Delwyn's Pressure Washing Services

Starting a pressure washing business on my own in Central Valley California, not too much experience so affordable, I do houses, fences, driveways, cars, trailers, RVs. Planning to make this full-time hoping clientele picks up after having a nice business card. Design doesn't have to be flashy, more to the point, I like simplistic/personable. I do not want something exhausting to look at or with too much going on.

Target Market(s)

Residential, Commercial

Industry/Entity Type

Pressure Washing

Contact Information for Business Card

avalible Services

Font styles to use
Sans Serif

Colors
0054AA
0677BA
7BADD7
CADEEF
E8F1F8
0094D4
00A9DD
6FCCEA
C7EBF8
E9F6FB
00AB8E
00BBA5
67D7C9
C6EFE9
E9F9F6

```html
<!DOCTYPE html>
<html lang="en">
<head>
<meta charset="UTF-8">
<title>Delwyn's Pressure Washing Services – Business Card</title>
<link href="https://fonts.googleapis.com/css2?family=Montserrat:wght@500;600;800&display=swap" rel="stylesheet">
<style>
  :root {
    --stage: #1b1b1d;
    --blue-deep: #0a2f8f;
    --blue-main: #0054AA;
    --blue-bright: #0677BA;
    --blue-vivid: #0a63d8;
    --blue-slate: #3c5a9a;
    --paper: #ffffff;
    --ink-light: #ffffff;
  }
  * { margin: 0; padding: 0; box-sizing: border-box; }
  html, body { width: 1200px; height: 1015px; overflow: hidden; }
  body {
    background: var(--stage);
    font-family: "Montserrat", Arial, sans-serif;
    position: relative;
  }
  .card {
    position: absolute;
    left: 250px;
    width: 700px;
    height: 400px;
    border-radius: 4px;
    overflow: hidden;
  }
  .card--front {
    top: 70px;
    background: radial-gradient(ellipse at 30% 10%, var(--blue-vivid) 0%, var(--blue-main) 45%, var(--blue-deep) 100%);
  }
  .card--back {
    top: 545px;
    background: var(--paper);
  }
  .front-pattern {
    position: absolute; inset: 0;
    background: linear-gradient(160deg, rgba(255,255,255,0.06), rgba(0,0,0,0.08));
  }
  .wordmark {
    position: absolute;
    color: var(--ink-light);
    font-weight: 600;
    text-transform: uppercase;
    line-height: 1;
  }
  .card--front .wordmark {
    left: 0; right: 0; top: 150px;
    text-align: center;
  }
  .wordmark__name { display: block; font-size: 64px; letter-spacing: 4px; }
  .wordmark__tag { display: block; font-size: 19px; letter-spacing: 1.5px; margin-top: 12px; }

  .card--back .wordmark {
    color: var(--blue-main);
    left: 60px; top: 120px;
  }
  .card--back .wordmark__name { font-size: 50px; letter-spacing: 3px; }
  .card--back .wordmark__tag { font-size: 15px; letter-spacing: 1.2px; margin-top: 10px; }

  .wave { position: absolute; inset: 0; width: 100%; height: 100%; }

  .contact {
    position: absolute;
    right: 34px; top: 215px;
    text-align: right;
    color: var(--ink-light);
  }
  .contact__name { font-weight: 800; font-size: 24px; }
  .contact__role { font-weight: 500; font-size: 15px; margin-bottom: 22px; }
  .contact__line {
    display: flex; justify-content: flex-end; align-items: center; gap: 8px;
    font-weight: 500; font-size: 17px; margin-top: 6px;
  }
  .contact__line svg { width: 15px; height: 15px; fill: var(--ink-light); }

  .social {
    position: absolute; left: 150px; bottom: 28px;
    display: flex; align-items: center; gap: 10px;
    color: var(--ink-light); font-weight: 500; font-size: 18px;
  }
  .social__dot {
    width: 18px; height: 18px; border: 2px solid var(--ink-light); border-radius: 50%;
  }
</style>
</head>
<body>

  <section class="card card--front" aria-label="Card front">
    <div class="front-pattern" role="img" aria-label="Faint repeated brand pattern on blue background"></div>
    <div class="wordmark">
      <span class="wordmark__name">Delwyn's</span>
      <span class="wordmark__tag">Pressure Washing Services</span>
    </div>
  </section>

  <section class="card card--back" aria-label="Card back">
    <svg class="wave" viewBox="0 0 700 400" preserveAspectRatio="none" aria-hidden="true">
      <defs>
        <linearGradient id="waveFill" x1="0" y1="1" x2="1" y2="0">
          <stop offset="0" stop-color="#0a63d8"/>
          <stop offset="1" stop-color="#0a3a9e"/>
        </linearGradient>
      </defs>
      <path d="M0 300 C 220 300, 320 250, 410 150 S 590 40 700 45 L700 60 C 600 58, 520 100, 440 190 S 240 320 0 320 Z" fill="#0a5fd0"/>
      <path d="M0 326 C 250 326, 350 250, 440 165 S 610 70 700 72 L700 80 C 610 80, 530 120, 455 195 S 250 334 0 334 Z" fill="var(--blue-slate)"/>
      <path d="M0 342 C 260 342, 370 260, 460 180 S 620 86 700 90 L700 400 L0 400 Z" fill="url(#waveFill)"/>
    </svg>

    <div class="wordmark">
      <span class="wordmark__name">Delwyn's</span>
      <span class="wordmark__tag">Pressure Washing Services</span>
    </div>

    <div class="contact">
      <div class="contact__name">Delwyn Marsh</div>
      <div class="contact__role">Owner</div>
      <div class="contact__line">(209)555-0147
        <svg viewBox="0 0 24 24"><path d="M6.6 10.8a15.1 15.1 0 0 0 6.6 6.6l2.2-2.2a1 1 0 0 1 1-.25 11.4 11.4 0 0 0 3.6.57 1 1 0 0 1 1 1V20a1 1 0 0 1-1 1A17 17 0 0 1 3 4a1 1 0 0 1 1-1h3.5a1 1 0 0 1 1 1c0 1.25.2 2.45.57 3.57a1 1 0 0 1-.25 1z"/></svg>
      </div>
      <div class="contact__line">DPWServices209@mailbox.com
        <svg viewBox="0 0 24 24"><path d="M2 5h20v14H2z M4 7v.5l8 5 8-5V7l-8 5z" fill-rule="evenodd"/></svg>
      </div>
    </div>

    <div class="social">
      <span class="social__dot"></span>
      <span>@DPW.Services</span>
    </div>
  </section>

</body>
</html>
```